Brusque Premium Men's Shaving Cream Product Label . Cream packaged in a Amber Jar/Black Top Cap.

Please include information ( see Brusque design Template attachment) designed on a Round Top cap. Label Diameter: 3.125" NOTE: Design this First,
Wrap Around Label: 11.3125 x 0.875" (w x h): NOTE: Required latter after selection of Final Design Selection.
Shave Cream packaged in an 8oz Low Profile Amber Jar/Black Top Cap.
Thanks

Target Market(s)

Prime Target-Men Ages 20yrs-65yrs+ and Women 20yrs-65yrs+( they purchase ovr 55% of these Mens care products for partner/spouse/friend.

Industry/Entity Type

Personel Care/Cosmetics/NaturalHealthcare

Other font styles liked:
• At this stage if you would like to submi a desigh that would include both a Top Label and your Wrap-around label on a Amber jar/black top lid. It would be helpful to see how it would look complete. Thanks . Please refer to the updated design Graphic Template for copy and layout . Questions? Let me know. Thanks.Please now use TIMBERLAND on label designs. Thanks! Please see image attachment for added Tree Image Vector that can be added to your design instead of the Original Tree Image .

Requirements
Must have
• Look and Feel of a Quality/Premium Mens Skincare Brand with a Masculine feel but attractive to women as well ( not Macho!).Think Unisex with a Male slant.
Nice to have
• Premium/Quality/Natural Skincare & Bodycare Brand
Should not have
• Not Macho. No Cartoony or Barber Tools/Bearded Men Images. Too gimicky and over-hyped!

```html
<!DOCTYPE html>
<html lang="en">
<head>
<meta charset="utf-8">
<title>Grovemere Premium Shaving Cream Label</title>
<link rel="stylesheet" href="https://fonts.googleapis.com/css2?family=Vollkorn:wght@400;700&family=Cabin+Condensed:wght@500&display=swap">
<style>
  :root {
    --canvas: #f6f6f6;
    --label-white: #f1f1f1;
    --teal: #00c1d0;
    --ink: #151515;
    --band-black: #242424;
    --tree-green: #6fae3a;
    --text-light: #ffffff;
  }
  * { margin: 0; padding: 0; box-sizing: border-box; }
  html, body {
    width: 1200px;
    height: 900px;
    overflow: hidden;
    background: var(--canvas);
  }
  .canvas {
    position: relative;
    width: 1200px;
    height: 900px;
  }
  .wrap-label {
    position: absolute;
    left: 150px;
    top: 234px;
    width: 900px;
    height: 432px;
    background: var(--label-white);
    color: var(--ink);
    text-align: center;
    font-family: "Vollkorn", Georgia, serif;
  }
  .top-strip {
    position: absolute;
    left: 0; top: 0;
    width: 100%;
    height: 12px;
    background: var(--teal);
  }
  .maker-name {
    position: absolute;
    left: 0; right: 0;
    top: 40px;
    font-size: 19px;
    font-weight: 700;
    letter-spacing: 3px;
    line-height: 1;
  }
  .product-name {
    position: absolute;
    left: 0; right: 0;
    top: 78px;
    font-size: 52px;
    font-weight: 700;
    letter-spacing: 1px;
    line-height: 1;
  }
  .product-tier {
    position: absolute;
    left: 0; right: 0;
    top: 128px;
    font-size: 30px;
    font-weight: 400;
    line-height: 1;
  }
  .tree-art {
    position: absolute;
    left: 405px;
    top: 168px;
    width: 90px;
    height: 116px;
  }
  .product-type {
    position: absolute;
    left: 0; right: 0;
    top: 287px;
    font-family: "Cabin Condensed", "Arial Narrow", sans-serif;
    font-weight: 500;
    font-size: 27px;
    font-variant: small-caps;
    letter-spacing: 0.5px;
    line-height: 1;
  }
  .language-band {
    position: absolute;
    left: 0; top: 317px;
    width: 100%;
    height: 41px;
    background: var(--band-black);
    color: var(--text-light);
    font-size: 25px;
    line-height: 41px;
  }
  .scent-band {
    position: absolute;
    left: 0; top: 358px;
    width: 100%;
    height: 74px;
    background: var(--teal);
    padding-top: 3px;
  }
  .scent-name {
    font-size: 23px;
    font-weight: 700;
    line-height: 1.05;
  }
  .scent-year {
    font-size: 14px;
    line-height: 1.1;
  }
  .net-weight {
    font-size: 14px;
    font-weight: 700;
    line-height: 1.3;
  }
</style>
</head>
<body>
<main class="canvas">
  <section class="wrap-label">
    <div class="top-strip"></div>
    <p class="maker-name">BRUSQUE</p>
    <h1 class="product-name">GROVEMERE</h1>
    <p class="product-tier">Premium</p>
    <svg class="tree-art" viewBox="0 0 90 116" role="img" aria-label="Illustration of a small tree with green leaves">
      <rect x="0" y="0" width="90" height="116" rx="8" fill="var(--tree-green)" opacity="0.55"/>
    </svg>
    <p class="product-type">Shaving Cream</p>
    <div class="language-band">Crème De Rasage</div>
    <div class="scent-band">
      <p class="scent-name">Cedarline Absolut</p>
      <p class="scent-year">1935</p>
      <p class="net-weight">150g e 5.3 oz</p>
    </div>
  </section>
</main>
</body>
</html>
```